My business is primarily as a Herbalist, using Iridology to diagnose areas of weakness and which body systems need support and then dispensing a Herbal tonic. I also do Reflexology, Aromatherapy, Craniosacral Therapy, Reiki and make Organic Herbal Tea Blends.I don't have a logo. I will also be needing to update my business cards soon, but firstly need labels for a new product I've devised - CLEAR MIND BREW.This tea is powdered and is a combination of 16 herbs which help to nourish the brain tissues & support circulation to the brain, helping to prevent & prolong Dementia while also improving energy & vitality.My business colour is Magenta. My name is Delia Voskaridou, so maybe just use DELIA on the label.Please print address & mobile at the base of the label.81 Tulloch Rd Ashbury 2193 NSW | 0438172604 | The label needs to be round & no larger than 6cm

Target Market(s)

Universal

Industry/Entity Type

Health And Wellness

Font styles to use
Serif

Colors
6b449b
a64599

Requirements
Must have
• Magenta colour as a background.This colour is my so called trademark.
• DELIA- as a logo
• I want some vintage designs of florals with modern design.
• ORGANIC Herbal TEA blends
• CLEAR MIND BREW
• 200g
• Address & mobile at the base of label
Nice to have
• An improvement to my business card design & outlay.
• I love vintage but I also want it current. Sophisticated & stylish.
• It needs to represent quality & longevity & trust.

```html
<!DOCTYPE html>
<html lang="en">
<head>
<meta charset="utf-8">
<title>DELIA – Clear Mind Brew Label</title>
<link rel="stylesheet" href="https://fonts.googleapis.com/css2?family=Cinzel:wght@400;500&family=PT+Sans+Narrow:wght@400;700&display=swap">
<style>
  :root {
    --page-bg: #ffffff;
    --label-magenta: #982372;
    --floral-tone: #86195f;
    --band-green: #6cbd45;
    --ink-white: #ffffff;
    --ink-black: #111111;
  }
  html, body {
    margin: 0;
    padding: 0;
    width: 1200px;
    height: 1200px;
    overflow: hidden;
    background: var(--page-bg);
  }
  .label {
    display: block;
    width: 1200px;
    height: 1200px;
  }
  .label__disc { fill: var(--label-magenta); }
  .label__floral { fill: url(#floralTone); }
  .label__band { fill: var(--band-green); }
  .brand-name {
    font-family: "Cinzel", "Trajan Pro", serif;
    font-weight: 400;
    font-size: 104px;
    letter-spacing: 2px;
    fill: var(--ink-white);
  }
  .product-title {
    font-family: "PT Sans Narrow", "Arial Narrow", sans-serif;
    font-weight: 700;
    font-size: 124px;
    fill: var(--ink-white);
  }
  .product-subtitle {
    font-family: "PT Sans Narrow", "Arial Narrow", sans-serif;
    font-weight: 700;
    font-size: 56px;
    fill: var(--ink-black);
  }
  .net-weight {
    font-family: "PT Sans Narrow", "Arial Narrow", sans-serif;
    font-weight: 700;
    font-size: 100px;
    fill: var(--ink-white);
  }
  .contact-line {
    font-family: "PT Sans Narrow", "Arial Narrow", sans-serif;
    font-weight: 700;
    font-size: 31px;
    fill: var(--ink-white);
  }
</style>
</head>
<body>
<svg class="label" viewBox="0 0 1200 1200" xmlns="http://www.w3.org/2000/svg">
  <defs>
    <clipPath id="discClip">
      <circle cx="600" cy="600" r="434"/>
    </clipPath>
    <radialGradient id="floralTone" cx="50%" cy="50%" r="50%">
      <stop offset="0%" stop-color="#86195f" stop-opacity="1"/>
      <stop offset="100%" stop-color="#982372" stop-opacity="0"/>
    </radialGradient>
  </defs>

  <circle class="label__disc" cx="600" cy="600" r="434"/>

  <g clip-path="url(#discClip)">
    <ellipse class="label__floral" cx="610" cy="620" rx="360" ry="290"
             role="img" aria-label="Vintage line-drawn floral bouquet of herbs, leaves and blossoms"/>
    <rect class="label__band" x="178" y="506" width="854" height="250"/>
  </g>

  <text class="brand-name" x="600" y="356" text-anchor="middle">DELIA</text>

  <text class="product-title" x="600" y="644" text-anchor="middle" textLength="780" lengthAdjust="spacingAndGlyphs">CLEAR MIND BREW</text>
  <text class="product-subtitle" x="600" y="720" text-anchor="middle" textLength="580" lengthAdjust="spacingAndGlyphs">ORGANIC Herbal TEA blends</text>

  <text class="net-weight" x="615" y="852" text-anchor="middle" textLength="166" lengthAdjust="spacingAndGlyphs">200 g</text>

  <text class="contact-line" x="610" y="908" text-anchor="middle">81 Tulloch Rd</text>
  <text class="contact-line" x="610" y="946" text-anchor="middle">Ashbury 2193 NSW</text>
  <text class="contact-line" x="610" y="990" text-anchor="middle">0438172604</text>
</svg>
</body>
</html>
```